Veltrionix Knowledge Enhancement Company Website

Veltrionix is knowledge enhancement Highend and Deep Technology Company who has training programs in Applied Quantum, Applied Artificial Intelligence and Data Science. All the technologies are very advanced and future technologies and the website should reflect the technology advancement. Looking for a sophisticated web design which will reflect our focus on deep and future technologies. Logo file is uploaded

Target Market(s)

Big Corporates and Premium Colleges

Industry/Entity Type

Technology, Deep Technology, Future Technology

Coding

Coded - Design and coding required

Number of Pages Required

5+ page

Requirements
Must have
• A Very Contemporary clean look and should reflect Future Technologies
Nice to have
• Should be very Classy
Should not have
• Traditional Fonts and Colors

```html
<!DOCTYPE html>
<html lang="en">
<head>
<meta charset="utf-8">
<title>Veltrionix</title>
<link rel="stylesheet" href="https://fonts.googleapis.com/css2?family=Playfair+Display:wght@400;700&family=Tinos:wght@400;700&display=swap">
<style>
:root{
  --blue:#2aa4de;
  --blue-deep:#2a8fc4;
  --blue-mid:#36a3d9;
  --blue-light:#4fc0f5;
  --navy:#0d4a6b;
  --ink:#1b1b1b;
  --text:#3a3a3a;
  --pale:#f3f6f9;
  --black:#0b0b0b;
  --white:#fff;
}
*{margin:0;padding:0;box-sizing:border-box}
html,body{width:1200px;height:4448px;overflow:hidden}
body{position:relative;background:var(--white);font-family:"Tinos",serif;color:var(--text)}
.abs{position:absolute}
h1,h2,h3{font-family:"Playfair Display",serif;font-weight:400;color:var(--ink)}
.btn{position:absolute;display:flex;align-items:center;justify-content:center;border:2px solid #333;font-size:11px;letter-spacing:.5px;text-transform:uppercase;color:#222;background:transparent}
.para{font-size:17px;line-height:27.5px;color:var(--text)}
.ph{position:absolute}

/* top bar */
.topbar{left:0;top:0;width:1200px;height:45px;background:var(--blue)}
.social-dot{position:absolute;width:24px;height:24px;border-radius:50%;background:rgba(255,255,255,.25);top:10px}
.contact-item{position:absolute;top:0;height:45px;display:flex;align-items:center;gap:9px;color:#fff;font-size:14px}
.ring{width:28px;height:28px;border:1.5px solid #fff;border-radius:50%}

/* nav */
.nav{left:0;top:45px;width:1200px;height:88px;background:#fff}
.brand{position:absolute;display:flex;align-items:center;gap:8px;font-family:"Tinos",serif;color:var(--blue)}
.brand .sq{background:var(--blue)}
.menu{position:absolute;right:102px;top:0;height:88px;display:flex;align-items:center;gap:52px;font-size:16px;color:#222}
.menu .active{color:var(--blue)}

/* hero */
.hero{left:0;top:133px;width:1200px;height:629px;background:linear-gradient(90deg,#0f3e66 0%,#1a4f80 45%,#2a6aa8 100%)}
.hero-art{left:0;top:0;width:660px;height:629px;background:radial-gradient(ellipse at 30% 45%,#2f86b3 0%,#174a75 55%,rgba(20,60,100,0) 100%)}
.hero h2{position:absolute;left:694px;top:172px;color:#fff;font-size:43px}
.hero h1{position:absolute;left:694px;top:220px;color:#fff;font-size:70px;font-weight:700}
.hero p{position:absolute;left:696px;top:322px;width:420px;color:#fff;font-size:17px;line-height:28px}
.hero .btn{left:696px;top:406px;width:147px;height:38px;border-color:#fff;color:#fff;font-size:12px}

/* training */
.training{left:0;top:1330px;width:1200px;height:1516px;background:var(--pale)}
.section-title{position:absolute;left:0;width:1200px;text-align:center;font-weight:700;font-size:48px;color:var(--ink)}
.vlabel{position:absolute;font-family:"Tinos",serif;font-weight:700;font-size:30px;letter-spacing:1px;color:transparent;-webkit-text-stroke:1.2px #888;writing-mode:vertical-rl;transform:rotate(180deg)}
.vline{position:absolute;width:1px;background:#bbb}
.band{position:absolute;height:104px}
.prog-title{position:absolute;font-size:34px}

/* testimonials */
.testimonial-panel{left:150px;top:2985px;width:910px;height:345px;background:var(--navy)}
.quote{position:absolute;left:330px;top:3070px;width:540px;text-align:center;color:#fff;font-size:17px;line-height:28px}
.quote-name{position:absolute;left:0;width:1200px;text-align:center;color:#fff}

/* blog */
.blog{left:0;top:3423px;width:1200px;height:592px;background:var(--pale)}
.blog-title{position:absolute;font-size:27px;line-height:39px;color:var(--ink)}

/* footer */
.footer{left:0;top:4015px;width:1200px;height:433px;background:var(--black);color:#fff}
.footer-heading{position:absolute;color:#fff;font-size:21px;font-weight:700}
.flinks{position:absolute;list-style:none;font-size:14px;line-height:28.5px;color:#fff}
.fcontact{position:absolute;display:flex;gap:10px;font-size:14px;line-height:20px;color:#fff}
.fcontact .ring{width:27px;height:27px;border-color:var(--blue);flex:none}
.fsocial{position:absolute;width:20px;height:20px;background:#444;top:4240px}
</style>
</head>
<body>

<!-- top bar -->
<div class="abs topbar">
  <span class="social-dot" style="left:103px"></span>
  <span class="social-dot" style="left:140px"></span>
  <span class="social-dot" style="left:177px"></span>
  <div class="contact-item" style="left:734px"><span class="ring"></span>+2 (555) 240 7300</div>
  <div class="contact-item" style="left:918px"><span class="ring"></span>info@veltrionix.com</div>
</div>

<!-- nav -->
<header class="abs nav">
  <div class="brand" style="left:102px;top:26px;font-size:17px"><span class="sq" style="width:34px;height:34px"></span>Veltrionix</div>
  <nav class="menu">
    <span class="active">Home</span><span>About Us</span><span>Training</span><span>Blog</span><span>Contact Us</span>
  </nav>
</header>

<!-- hero -->
<section class="abs hero">
  <div class="ph hero-art" role="img" aria-label="Profile of a man with a glowing digital circuit network across his head"></div>
  <h2>Quantum</h2>
  <h1>Computing</h1>
  <p>Could be the most significant technological revolution since the internet's inception.</p>
  <span class="btn">Get Started</span>
</section>

<!-- welcome -->
<section>
  <div class="abs" style="left:102px;top:884px;font-size:17px;color:#222">Welcome To</div>
  <h2 class="abs" style="left:102px;top:900px;font-size:48px;font-weight:700">Veltrionix</h2>
  <p class="abs para" style="left:102px;top:1000px;width:485px">Quantum computing could be the most significant technological revolution since the internet's inception. According to experts, the market for quantum technologies will quadruple by 2029. There has never been a better time to get involved in a thriving industry like quantum computing.</p>
  <span class="btn" style="left:102px;top:1169px;width:118px;height:36px">About Us</span>
  <div class="ph" role="img" aria-label="Brand emblem filled with a photo of people working at computers" style="left:670px;top:838px;width:427px;height:414px;background:radial-gradient(circle at 60% 55%,#3e8fc2 0%,#1c6aa3 55%,#f3f7fb 100%)"></div>
</section>

<!-- training -->
<section class="abs training"></section>
<h2 class="section-title" style="top:1405px">Training Programs</h2>

<!-- row 1 -->
<div class="band" style="left:0;top:1775px;width:547px;background:var(--blue-deep)"></div>
<span class="vlabel" style="left:96px;top:1528px">QUANTUM</span>
<span class="vline" style="left:112px;top:1705px;height:120px"></span>
<div class="ph" role="img" aria-label="Person wearing a VR headset interacting with holographic data screens" style="left:166px;top:1530px;width:361px;height:295px;background:linear-gradient(135deg,#0d2f57,#2b6fa6 60%,#123c6a)"></div>
<h3 class="prog-title" style="left:611px;top:1520px">Applied Quantum</h3>
<p class="abs para" style="left:611px;top:1598px;width:460px">Nor again is there anyone who loves or pursues or desires to obtain pain of itself, because it is pain, but because occasionally circumstances occur in which toil and pain can procure him some great pleasure. To take a trivial example, which of us ever undertakes laborious physical exercise</p>
<span class="btn" style="left:611px;top:1774px;width:118px;height:35px">Read More</span>

<!-- row 2 -->
<div class="band" style="left:653px;top:2214px;width:547px;background:var(--blue-mid)"></div>
<span class="vlabel" style="left:1071px;top:1966px">INTELLIGENCE</span>
<span class="vline" style="left:1086px;top:2214px;height:50px"></span>
<div class="ph" role="img" aria-label="White humanoid robot working at a laptop in a bright office" style="left:673px;top:1969px;width:360px;height:295px;background:linear-gradient(135deg,#e4c9b3,#b9c4d2 45%,#6f8aa6)"></div>
<h3 class="prog-title" style="left:189px;top:1960px;width:400px;text-align:right;line-height:41px">Applied<br>Artificial Intelligence</h3>
<p class="abs para" style="left:129px;top:2064px;width:460px;text-align:right">Nor again is there anyone who loves or pursues or desires to obtain pain of itself, because it is pain, but because occasionally circumstances occur in which toil and pain can procure him some great pleasure. To take a trivial example, which of us ever undertakes laborious physical exercise</p>
<span class="btn" style="left:471px;top:2247px;width:118px;height:35px">Read More</span>

<!-- row 3 -->
<div class="band" style="left:0;top:2654px;width:547px;background:var(--blue-light)"></div>
<span class="vlabel" style="left:96px;top:2404px">SCIENCE</span>
<span class="vline" style="left:112px;top:2555px;height:150px"></span>
<div class="ph" role="img" aria-label="Hands holding a tablet showing data dashboards" style="left:166px;top:2409px;width:361px;height:295px;background:linear-gradient(135deg,#eef1f4,#c9d3dc 40%,#1d3550 60%,#e4e8ec)"></div>
<h3 class="prog-title" style="left:611px;top:2397px">Data Science</h3>
<p class="abs para" style="left:611px;top:2474px;width:460px">Nor again is there anyone who loves or pursues or desires to obtain pain of itself, because it is pain, but because occasionally circumstances occur in which toil and pain can procure him some great pleasure. To take a trivial example, which of us ever undertakes laborious physical exercise</p>
<span class="btn" style="left:612px;top:2642px;width:118px;height:35px">Read More</span>

<!-- testimonials -->
<h2 class="section-title" style="top:2905px">Testimonials</h2>
<div class="ph testimonial-panel" role="img" aria-label="Dark navy painted brush-stroke backdrop behind the testimonial"></div>
<p class="quote">Sed ut perspiciatis unde omnis iste natus error sit voluptatem accusantium doloremque laudantium, totam rem aperiam, eaque ipsa quae ab illo inventore veritatis et quasi architecto beatae vitae dicta sunt explicabo.</p>
<div class="quote-name" style="top:3212px;font-family:'Playfair Display',serif;font-weight:700;font-size:20px">Orlen Vastry</div>
<div class="quote-name" style="top:3241px;font-size:10px">Consultant</div>
<div class="abs" style="left:568px;top:3290px;width:20px;height:3px;background:var(--blue)"></div>
<div class="abs" style="left:591px;top:3290px;width:20px;height:3px;background:#cfd8e0"></div>
<div class="abs" style="left:614px;top:3290px;width:20px;height:3px;background:#cfd8e0"></div>

<!-- blog -->
<section class="abs blog"></section>
<h2 class="section-title" style="top:3473px;font-size:46px">Recent Blog</h2>
<p class="abs" style="left:0;top:3541px;width:1200px;text-align:center;font-size:15px;color:#222">Sed ut perspiciatis unde omnis iste natus error sit voluptatem</p>

<div class="ph" role="img" aria-label="Businessman in a suit looking at the camera" style="left:102px;top:3592px;width:318px;height:208px;background:linear-gradient(135deg,#2b3440,#6a7684 55%,#c8ced5)"></div>
<div class="ph" role="img" aria-label="Presenter at a whiteboard with colleagues at a table" style="left:442px;top:3592px;width:318px;height:208px;background:linear-gradient(135deg,#2a4a8a,#e6e8ec 55%,#9aa4b0)"></div>
<div class="ph" role="img" aria-label="Team working at computers in front of a world map" style="left:781px;top:3592px;width:317px;height:208px;background:linear-gradient(135deg,#c9ccd0,#555d66 55%,#a7adb4)"></div>

<h3 class="blog-title" style="left:102px;top:3822px">Denouncing pleasure and<br>praising pain</h3>
<h3 class="blog-title" style="left:442px;top:3822px">Sed ut perspiciatis unde<br>omnis iste</h3>
<h3 class="blog-title" style="left:781px;top:3822px">Denouncing pleasure and<br>praising pain</h3>
<span class="btn" style="left:102px;top:3915px;width:118px;height:35px">Read More</span>
<span class="btn" style="left:442px;top:3915px;width:118px;height:35px">Read More</span>
<span class="btn" style="left:781px;top:3915px;width:118px;height:35px">Read More</span>

<!-- footer -->
<footer class="abs footer"></footer>
<div class="brand" style="left:102px;top:4100px;font-size:17px"><span class="sq" style="width:60px;height:60px"></span>Veltrionix</div>
<span class="fsocial" style="left:105px"></span>
<span class="fsocial" style="left:134px"></span>
<span class="fsocial" style="left:163px"></span>

<h3 class="footer-heading" style="left:399px;top:4080px">Quick Links</h3>
<ul class="flinks" style="left:399px;top:4120px"><li>Home</li><li>About Us</li><li>Training</li><li>Blog</li><li>Contact Us</li></ul>

<h3 class="footer-heading" style="left:594px;top:4080px">Training</h3>
<ul class="flinks" style="left:594px;top:4120px"><li>Applied Quantum</li><li>Applied Artificial Intelligence</li><li>Data Science</li></ul>

<h3 class="footer-heading" style="left:853px;top:4080px">Contacts</h3>
<div class="fcontact" style="left:853px;top:4124px;width:260px"><span class="ring"></span><span>14/B Lorem ipsum dolar sit amet<br>Norbridge 31kpo UKE</span></div>
<div class="fcontact" style="left:853px;top:4182px;align-items:center"><span class="ring"></span><span>+2 (555) 240 7300</span></div>
<div class="fcontact" style="left:853px;top:4228px;align-items:center"><span class="ring"></span><span>info@veltrionix.com</span></div>

<p class="abs" style="left:0;top:4368px;width:1200px;text-align:center;color:#fff;font-size:11px">Copyright © 2023 <span style="color:var(--blue)">Veltrionix</span>. All rights reserved.</p>

</body>
</html>
```